Tallowood plumbing plumbing company business card design

Something sinilar to business card i upload it is my old business card design
And have a good watermark with the logo or majority of the logot in rhe background as watermark

Plumbing business similar to uploaded design with a nice watermark of the logo

Font styles to use
Script

Colors

Designer to choose colors to be used in the design.

```html
<!DOCTYPE html>
<html lang="en">
<head>
<meta charset="UTF-8">
<title>Tallowood Plumbing – Business Card</title>
<link rel="stylesheet" href="https://fonts.googleapis.com/css2?family=Montserrat:wght@600&family=Roboto:wght@400;500;700&display=swap">
<style>
  :root {
    --stage: #262626;
    --card-light: #eeeeef;
    --card-dark: #0c0c0d;
    --brand-blue: #0d5aa0;
    --accent-blue: #2b8fd8;
    --ink: #151515;
    --white: #ffffff;
    --tap-grey: #3a3d40;
    --tap-outline: #e6e6e6;
    --watermark: #25272a;
    --muted: #b9bcc0;
  }
  * { margin: 0; padding: 0; box-sizing: border-box; }
  html, body {
    width: 1200px; height: 576px; overflow: hidden;
    background: var(--stage);
    font-family: "Roboto", Arial, sans-serif;
  }
  .card {
    position: absolute;
    border-radius: 14px;
    overflow: hidden;
    box-shadow: 0 4px 10px rgba(0,0,0,.45);
  }
  /* Front */
  .card-front { left: 81px; top: 138px; width: 485px; height: 294px; background: var(--card-light); }
  .front-brand {
    position: absolute; left: 22px; top: 36px;
    display: flex; align-items: center; gap: 12px;
  }
  .brand-square { width: 22px; height: 22px; background: var(--brand-blue); }
  .brand-name {
    font-family: "Montserrat", Arial, sans-serif; font-weight: 600;
    font-size: 20px; letter-spacing: 3.5px; text-transform: uppercase;
    color: var(--ink);
  }
  .contact-band {
    position: absolute; left: 0; top: 106px; width: 100%; height: 145px;
    background: var(--brand-blue);
  }
  .tap-illustration {
    position: absolute; left: 266px; top: 106px; width: 219px; height: 188px;
    background: var(--tap-grey);
    border-top-left-radius: 16px;
    border: 5px solid var(--tap-outline); border-right: none; border-bottom: none;
  }
  .person { position: absolute; left: 21px; top: 123px; color: var(--white); }
  .person-name { font-weight: 700; font-size: 20px; letter-spacing: .3px; }
  .person-role { font-size: 13px; margin-top: 4px; color: #e4ecf5; }
  .contact-list {
    position: absolute; left: 21px; top: 181px; list-style: none;
    color: var(--white); font-size: 12.5px;
  }
  .contact-list li { display: flex; align-items: center; gap: 10px; height: 19px; }
  .contact-list svg { width: 12px; height: 12px; fill: var(--white); }
  .address {
    position: absolute; left: 21px; top: 266px;
    font-size: 12.5px; color: var(--ink);
  }
  /* Back */
  .card-back { left: 602px; top: 138px; width: 480px; height: 292px; background: var(--card-dark); }
  .tap-watermark {
    position: absolute; left: 0; top: 34px; width: 186px; height: 224px;
    background: var(--watermark); border-top-right-radius: 20px;
  }
  .back-brand {
    position: absolute; right: 34px; top: 88px;
    display: flex; align-items: center; gap: 12px;
  }
  .back-brand .brand-square { width: 26px; height: 26px; background: var(--accent-blue); }
  .back-brand .brand-name { color: var(--white); font-size: 24px; letter-spacing: 4px; }
  .web {
    position: absolute; right: 34px; top: 246px;
    font-size: 12.5px; color: var(--muted);
  }
  .web .domain { color: var(--accent-blue); }
</style>
</head>
<body>
  <section class="card card-front">
    <div class="front-brand">
      <span class="brand-square"></span>
      <span class="brand-name">Tallowood Plumbing</span>
    </div>
    <div class="contact-band"></div>
    <div class="tap-illustration" role="img" aria-label="Large illustrated water tap in dark grey with a light outline"></div>
    <div class="person">
      <div class="person-name">MARCUS HALE</div>
      <div class="person-role">Managing Principal</div>
    </div>
    <ul class="contact-list">
      <li><svg viewBox="0 0 24 24"><path d="M6.6 10.8a15.1 15.1 0 0 0 6.6 6.6l2.2-2.2a1 1 0 0 1 1-.25 11.4 11.4 0 0 0 3.6.57 1 1 0 0 1 1 1V20a1 1 0 0 1-1 1A17 17 0 0 1 3 4a1 1 0 0 1 1-1h3.5a1 1 0 0 1 1 1c0 1.25.2 2.46.57 3.6a1 1 0 0 1-.25 1z"/></svg>555-0142-7788</li>
      <li><svg viewBox="0 0 24 24"><path d="M2 5h20v14H2z M4 7v.5l8 5 8-5V7l-8 5z" fill-rule="evenodd"/></svg>marcus@tallowoodplumbing.com</li>
      <li><svg viewBox="0 0 24 24"><path d="M12 2a10 10 0 1 0 0 20 10 10 0 0 0 0-20zm6.9 6h-3a15 15 0 0 0-1.3-4 8 8 0 0 1 4.3 4zM12 4c.8 1.2 1.5 2.5 1.9 4h-3.8c.4-1.5 1.1-2.8 1.9-4zM4.3 14a8 8 0 0 1 0-4h3.4a16 16 0 0 0 0 4zm.8 2h3a15 15 0 0 0 1.3 4 8 8 0 0 1-4.3-4zm3-8h-3a8 8 0 0 1 4.3-4 15 15 0 0 0-1.3 4zM12 20c-.8-1.2-1.5-2.5-1.9-4h3.8c-.4 1.5-1.1 2.8-1.9 4zm2.3-6H9.7a14 14 0 0 1 0-4h4.6a14 14 0 0 1 0 4zm.3 6a15 15 0 0 0 1.3-4h3a8 8 0 0 1-4.3 4zm1.7-6a16 16 0 0 0 0-4h3.4a8 8 0 0 1 0 4z"/></svg>www.tallowoodplumbing.com</li>
    </ul>
    <div class="address">18 Harbour Lane, Riverside, Tallowood 2145</div>
  </section>

  <section class="card card-back">
    <div class="tap-watermark" role="img" aria-label="Faint oversized water tap watermark"></div>
    <div class="back-brand">
      <span class="brand-square"></span>
      <span class="brand-name">Tallowood Plumbing</span>
    </div>
    <div class="web">www.<span class="domain">tallowoodplumbing</span>.com</div>
  </section>
</body>
</html>
```